Coastal Bright Sweep Business Card

We are a cleaning and waste management company with the slogan "making waste to landfill a thing of the past". We would like a re-design of our current business card. On the front we want to continue to use our logo as the focus point. On the back, we want the whole thing re-done to be less busy. We want the staff member’s name, the job title, mobile number, email and website. We do not want the address on the card. We still want the green, black and blue colours used, but a new font for the information on the back. Please do not change the logo design at all. We are also thinking about using icons to replace the text ‘mobile, email, website’. The “events + commercial” banner needs to be incorporated somewhere and needs to read “events + commercial + waste”. Another important point for consideration is that we are very concerned about being environmentally sustainable and will be printing on recycled paper. All designs should be made to compliment this in regards to boldness and colouring. Please find attached our logo, our colour chart and an image of our current business card.

```html
<!DOCTYPE html>
<html lang="en">
<head>
<meta charset="utf-8">
<title>Coastal Bright Sweep Business Card</title>
<link href="https://fonts.googleapis.com/css2?family=Montserrat:wght@600;700&family=Questrial&display=swap" rel="stylesheet">
<style>
  :root {
    --bg-light: #4f9a45;
    --bg-dark: #146a35;
    --navy: #123a66;
    --lime: #8abf3f;
    --sky: #1f9ad8;
    --white: #ffffff;
    --ink: #0f2740;
  }
  * { margin: 0; padding: 0; box-sizing: border-box; }
  html, body { width: 1200px; height: 888px; overflow: hidden; }
  body {
    background: radial-gradient(circle at 35% 40%, var(--bg-light), var(--bg-dark) 85%);
    font-family: "Questrial", "Century Gothic", sans-serif;
    position: relative;
  }
  .card {
    position: absolute;
    width: 520px;
    height: 300px;
    overflow: hidden;
    background: var(--lime);
    box-shadow: 0 10px 24px rgba(0, 0, 0, 0.35);
  }
  .card-shapes { position: absolute; inset: 0; width: 100%; height: 100%; }

  /* Front */
  .card-front { left: 60px; top: 110px; }
  .brand-name {
    position: absolute;
    left: 40px;
    top: 105px;
    width: 240px;
    font-family: "Montserrat", sans-serif;
    font-weight: 700;
    font-size: 34px;
    line-height: 1.05;
    color: var(--white);
  }
  .front-web {
    position: absolute;
    right: 22px;
    bottom: 22px;
    font-size: 10px;
    letter-spacing: 3px;
    color: var(--white);
  }

  /* Back */
  .card-back { left: 620px; top: 470px; }
  .back-brand {
    position: absolute;
    right: 26px;
    top: 26px;
    width: 150px;
    text-align: right;
    font-family: "Montserrat", sans-serif;
    font-weight: 700;
    font-size: 20px;
    line-height: 1.05;
    color: var(--navy);
  }
  .staff { position: absolute; left: 34px; top: 86px; color: var(--white); }
  .staff-name {
    font-family: "Montserrat", sans-serif;
    font-weight: 700;
    font-size: 26px;
    letter-spacing: 0.5px;
    text-transform: uppercase;
  }
  .staff-title { font-size: 17px; margin-left: 64px; margin-top: 2px; }
  .contact-list {
    position: absolute;
    left: 34px;
    top: 168px;
    list-style: none;
    color: var(--white);
    font-size: 15px;
  }
  .contact-list li { display: flex; align-items: center; gap: 10px; height: 22px; }
  .contact-icon { width: 16px; height: 16px; flex: none; }
  .service-banner {
    position: absolute;
    left: 0;
    right: 0;
    bottom: 16px;
    height: 30px;
    display: flex;
    align-items: center;
    justify-content: center;
    background: linear-gradient(90deg, rgba(138,191,63,0) 0%, rgba(15,39,64,0.85) 45%, rgba(15,39,64,0.85) 55%, rgba(138,191,63,0) 100%);
    color: var(--white);
    font-size: 15px;
    letter-spacing: 7px;
  }
</style>
</head>
<body>

  <section class="card card-front" aria-label="Card front">
    <svg class="card-shapes" viewBox="0 0 520 300" preserveAspectRatio="none" aria-hidden="true">
      <polygon points="0,0 318,0 262,300 0,300" fill="var(--navy)"/>
      <polygon points="318,0 326,0 276,300 262,300" fill="var(--white)"/>
    </svg>
    <div class="brand-name">Coastal Bright Sweep</div>
    <div class="front-web">www.coastalbrightsweep.com.au</div>
  </section>

  <section class="card card-back" aria-label="Card back">
    <svg class="card-shapes" viewBox="0 0 520 300" preserveAspectRatio="none" aria-hidden="true">
      <polygon points="200,0 232,0 520,220 520,248" fill="var(--sky)"/>
    </svg>
    <div class="back-brand">Coastal Bright Sweep</div>
    <div class="staff">
      <div class="staff-name">Jordan Pemberley</div>
      <div class="staff-title">Client Manager</div>
    </div>
    <ul class="contact-list">
      <li>
        <svg class="contact-icon" viewBox="0 0 16 16" aria-label="Mobile"><rect x="4" y="1" width="8" height="14" rx="1.5" fill="none" stroke="var(--white)" stroke-width="1.5"/><line x1="7" y1="12.5" x2="9" y2="12.5" stroke="var(--white)" stroke-width="1.5"/></svg>
        <span>0400 555 218</span>
      </li>
      <li>
        <svg class="contact-icon" viewBox="0 0 16 16" aria-label="Email"><rect x="1" y="3.5" width="14" height="9" fill="none" stroke="var(--white)" stroke-width="1.4"/><polyline points="1,3.5 8,9 15,3.5" fill="none" stroke="var(--white)" stroke-width="1.4"/></svg>
        <span>jpemberley@coastalbrightsweep.com.au</span>
      </li>
      <li>
        <svg class="contact-icon" viewBox="0 0 16 16" aria-label="Website"><circle cx="8" cy="8" r="6.5" fill="none" stroke="var(--white)" stroke-width="1.4"/><ellipse cx="8" cy="8" rx="3" ry="6.5" fill="none" stroke="var(--white)" stroke-width="1.2"/><line x1="1.5" y1="8" x2="14.5" y2="8" stroke="var(--white)" stroke-width="1.2"/></svg>
        <span>www.coastalbrightsweep.com.au</span>
      </li>
    </ul>
    <div class="service-banner">events + commercial + waste</div>
  </section>

</body>
</html>
```